Uprising SaaS company needs an attractive business card design

We're an uprising SaaS company who's attempting to attack the rigid car (insurance) claims management market in Europe.
We want to our mighty base order management system, listen to our clients to connect the smart ideas to build something even mightier.
We primarily focus on helping our customers manage their customers' claims/orders and get them resolved as smoothly as possible.
We'd like the business card design to express technical innovation and the fact that we connect smart ideas, as our company slogan indicates.
Contact Information for Business Card
Name, position, website, email, mobile, business address
Colors
Designer to choose colors to be used in the design.
Look and feel
Each slider illustrates characteristics of the customer's brand and the style your logo design should communicate.

```html
<!DOCTYPE html>
<html lang="en">
<head>
<meta charset="utf-8">
<title>Velonexa Business Card</title>
<link rel="stylesheet" href="https://fonts.googleapis.com/css2?family=Poppins:wght@300;400;500&display=swap">
<style>
  :root {
    --backdrop: #0e0e0f;
    --card: #2a2b2d;
    --card-back: #262729;
    --accent: #72c9de;
    --text-grey: #8a8b8d;
    --text-light: #d8d9db;
    --rule: #55575a;
    --emboss: #3a3b3e;
  }
  * { margin: 0; padding: 0; box-sizing: border-box; }
  html, body {
    width: 1200px; height: 820px; overflow: hidden;
    background: var(--backdrop);
    font-family: "Poppins", sans-serif;
  }
  .stage {
    position: relative; width: 1200px; height: 820px;
    display: flex; align-items: center; justify-content: center; gap: 40px;
  }
  .card {
    position: relative; width: 540px; height: 309px;
    background: var(--card);
    box-shadow: 0 10px 30px rgba(0,0,0,.6);
  }
  .card--front { border-left: 3px solid var(--accent); border-bottom: 3px solid var(--accent); }
  .card--back {
    background: var(--card-back);
    border-right: 4px solid var(--accent); border-bottom: 4px solid var(--accent);
    display: flex; align-items: center; justify-content: center;
  }
  .brand {
    position: absolute; right: 40px; top: 42px;
    font-weight: 300; font-size: 52px; letter-spacing: 1px;
    color: var(--text-grey); line-height: 1;
  }
  .brand-dot {
    display: inline-block; width: 10px; height: 10px; border-radius: 50%;
    background: var(--accent); margin-left: 6px; vertical-align: top; margin-top: 6px;
  }
  .divider {
    position: absolute; left: 40px; right: 40px; top: 142px;
    height: 1px; background: var(--rule);
  }
  .person { position: absolute; left: 40px; top: 165px; }
  .person-name { font-size: 21px; font-weight: 500; color: var(--text-grey); line-height: 1.2; }
  .person-name .surname { color: var(--accent); }
  .person-role { font-size: 13px; color: var(--text-light); font-weight: 400; }
  .person-rule { width: 130px; height: 1px; background: var(--rule); margin: 10px 0 8px; }
  .contacts { list-style: none; }
  .contacts li {
    display: flex; align-items: center; gap: 8px;
    font-size: 13px; color: var(--text-light); line-height: 1.5;
  }
  .contacts svg { width: 12px; height: 12px; flex: none; }
  .address {
    position: absolute; right: 40px; top: 165px; text-align: right;
    font-size: 13px; color: var(--text-light); line-height: 1.45;
  }
  .brand--embossed {
    position: static; font-size: 56px; color: var(--emboss);
    text-shadow: 0 -1px 0 rgba(0,0,0,.5), 0 1px 0 rgba(255,255,255,.06);
  }
</style>
</head>
<body>
<main class="stage">
  <section class="card card--front">
    <div class="brand">velonexa<span class="brand-dot"></span></div>
    <div class="divider"></div>
    <div class="person">
      <p class="person-name">Marcus <span class="surname">Hale</span></p>
      <p class="person-role">Managing Director</p>
      <div class="person-rule"></div>
      <ul class="contacts">
        <li>
          <svg viewBox="0 0 24 24" fill="none" stroke="var(--accent)" stroke-width="2.4"><path d="M5 3h4l2 5-3 2a11 11 0 0 0 6 6l2-3 5 2v4a2 2 0 0 1-2 2A17 17 0 0 1 3 5a2 2 0 0 1 2-2z"/></svg>
          044-987 654 321
        </li>
        <li>
          <svg viewBox="0 0 24 24" fill="var(--accent)"><path d="M2 5h20v14H2z"/><path d="M2 5l10 8 10-8" fill="none" stroke="var(--card)" stroke-width="2"/></svg>
          hello@velonexa.io
        </li>
        <li>
          <svg viewBox="0 0 24 24" fill="none" stroke="var(--accent)" stroke-width="2"><circle cx="12" cy="12" r="10"/><path d="M2 12h20M12 2c3 3 3 17 0 20M12 2c-3 3-3 17 0 20"/></svg>
          www.velonexa.io
        </li>
      </ul>
    </div>
    <address class="address" style="font-style:normal">
      421, Address line goes here<br>45452, Country Name
    </address>
  </section>

  <section class="card card--back">
    <div class="brand brand--embossed">velonexa</div>
  </section>
</main>
</body>
</html>
```